Workout book cover design: Looking for Simple Classic Cover

I need a book cover design for "Lift the Willow Line". A book on exercises to strengthen the pelvic floor. Basically it's exercises for your torso and hips. I want something tasteful and classic looking.

I like this book cover design: http://www.quellobranto.com/Calm-Starters-Gentle-Movements-Ease-ebook/dp/K93620QX51/ref=sr_1_40?ie=UTF8&qid=1447940424&sr=8-40&keywords=exercise+books

Book Title: Lift the Willow Line
Description to go under title: I'm working on that now and will have ready by the end of the project. (The hidden world of pelvic floor training. Discover the best exercises for creating a strong core, hips and pelvis today!)

Target Market(s)

Mostly women 35-65 and men 60+

Industry/Entity Type

Health And Wellness

Requirements
Must have
• ebook dementions: 1536 x 2048 I think works for all the online publishing companies
• 8x10 for print
Nice to have
• I like this book cover design: http://www.quellobranto.com/Calm-Starters-Gentle-Movements-Ease-ebook/dp/K93620QX51/ref=sr_1_40?ie=UTF8&qid=1447940424&sr=8-40&keywords=exercise+books
• This cover is also ok, but no shiny. http://www.quellobranto.com/Bedrock-Reshape-Daily-Master-Courage/dp/4827503916/ref=sr_1_2?ie=UTF8&qid=1447949910&sr=8-2&keywords=bedrock+book
Should not have
• I do not like this cover, it's crowded. http://www.quellobranto.com/Training-Endurance-Calisthenic-flexibility-endurance-ebook/dp/R77WPLNEKZ/ref=sr_1_2?ie=UTF8&qid=1447942094&sr=8-2&keywords=workout+books
• I do not want anyone on the cover making eye contact.

```html
<!DOCTYPE html>
<html lang="en">
<head>
<meta charset="utf-8">
<title>Lift the Willow Line — Book Cover</title>
<link rel="stylesheet" href="https://fonts.googleapis.com/css2?family=Antonio:wght@100;200&family=Libre+Baskerville:ital@0;1&family=Montserrat:wght@300;400;700&display=swap">
<style>
  :root {
    --stage: #ebe7ee;
    --cream: #fbf8e6;
    --rose: #c07479;
    --grey-text: #8d8a86;
    --grey-light: #b7b4af;
    --teal: #5fe3dd;
    --band: #76e8e0;
    --white: #ffffff;
    --sun-yellow: #fbeea8;
    --sun-orange: #f0b878;
    --sea-lilac: #b3a6c2;
    --sea-teal: #8fbcc0;
  }
  * { margin: 0; padding: 0; box-sizing: border-box; }
  html, body {
    width: 1200px;
    height: 1200px;
    overflow: hidden;
    background: var(--stage);
  }
  .cover {
    position: absolute;
    left: 187px;
    top: 50px;
    width: 825px;
    height: 1100px;
    background: var(--cream);
    overflow: hidden;
    box-shadow: 0 10px 30px rgba(80, 60, 90, 0.18);
  }
  .cover-photo {
    position: absolute;
    left: 0;
    top: 520px;
    width: 825px;
    height: 515px;
    display: block;
  }
  .headline {
    position: absolute;
    top: 58px;
    left: 0;
    width: 100%;
    text-align: center;
    font-family: "Montserrat", sans-serif;
    font-weight: 700;
    font-size: 22px;
    line-height: 1.3;
    letter-spacing: 0.14em;
    color: var(--rose);
  }
  .promise {
    position: absolute;
    top: 128px;
    left: 60px;
    width: 705px;
    text-align: center;
    font-family: "Montserrat", sans-serif;
    font-weight: 400;
    font-size: 15px;
    line-height: 1.35;
    text-transform: uppercase;
    color: var(--grey-text);
  }
  .title-lead {
    position: absolute;
    top: 196px;
    left: 0;
    width: 100%;
    text-align: center;
    font-family: "Montserrat", sans-serif;
    font-weight: 300;
    font-size: 46px;
    letter-spacing: 0.32em;
    color: var(--grey-light);
  }
  .title-main {
    position: absolute;
    top: 250px;
    left: 0;
    width: 100%;
    text-align: center;
    font-family: "Antonio", sans-serif;
    font-weight: 100;
    font-size: 178px;
    line-height: 1;
    letter-spacing: 0.01em;
    color: var(--teal);
    white-space: nowrap;
  }
  .tagline {
    position: absolute;
    top: 458px;
    left: 0;
    width: 100%;
    text-align: center;
    font-family: "Libre Baskerville", serif;
    font-style: italic;
    color: var(--grey-text);
  }
  .tagline-lead { font-size: 28px; line-height: 1.2; }
  .tagline-sub { font-size: 16px; line-height: 1.6; }
  .divider {
    position: absolute;
    top: 552px;
    left: 404px;
    width: 17px;
    height: 17px;
    background: #c9c6c2;
    transform: rotate(45deg);
  }
  .author-band {
    position: absolute;
    left: 0;
    bottom: 0;
    width: 100%;
    height: 66px;
    background: var(--band);
    display: flex;
    align-items: center;
    justify-content: center;
    font-family: "Libre Baskerville", serif;
    font-size: 19px;
    letter-spacing: 0.16em;
    color: var(--white);
  }
</style>
</head>
<body>
  <main class="cover">
    <svg class="cover-photo" viewBox="0 0 825 515" role="img" aria-label="Photo of a woman seen from behind, arms raised in triumph, facing a golden sunset over the sea">
      <defs>
        <linearGradient id="sky-to-sea" x1="0" y1="0" x2="0" y2="1">
          <stop offset="0" stop-color="#fbf8e6" stop-opacity="0"/>
          <stop offset="0.35" stop-color="#fbf1c4"/>
          <stop offset="0.58" stop-color="#f6d59a"/>
          <stop offset="0.68" stop-color="#b3a6c2"/>
          <stop offset="1" stop-color="#8fbcc0"/>
        </linearGradient>
        <radialGradient id="sun-glow" cx="0.62" cy="0.66" r="0.45">
          <stop offset="0" stop-color="#fff6c8" stop-opacity="0.95"/>
          <stop offset="1" stop-color="#f0b878" stop-opacity="0"/>
        </radialGradient>
      </defs>
      <rect width="825" height="515" fill="url(#sky-to-sea)"/>
      <rect width="825" height="515" fill="url(#sun-glow)"/>
    </svg>

    <p class="headline">THE PERFECT PELVIC FLOOR TRAINING FOR<br>MEN AND WOMEN</p>
    <p class="promise">The exercises are gentle and safe. They're also fun to do and easy<br>to fit into your daily routine, and the success is immediate.</p>

    <h1>
      <span class="title-lead">LIFT THE</span>
      <span class="title-main">WILLOW LINE</span>
    </h1>

    <div class="tagline">
      <p class="tagline-lead">The hidden world of pelvic floor training.</p>
      <p class="tagline-sub">Discover the best exercises for creating a strong core, hips and pelvis today!</p>
    </div>

    <span class="divider"></span>

    <footer class="author-band">BOOK AUTHOR</footer>
  </main>
</body>
</html>
```